New Business Card Design Project - RK Ledgerwise & Filing Partners, LLC

Below is a sample image of the card (TM Bookkeeping). I would like to have a designed business card that looks very similar (Front & Back). In addition, I would like to keep the same colors as well. I attached my Business Logo (RK Ledgerwise & Filing Partners, LLC) that will be on my website.

Target Market(s)

Executives, Business Owners, Board of Directors, Chief Financial Officers

Contact Information for Business Card

Font styles to use
Serif

Colors
0c5ba6
ffffff
5c5c5c

Requirements
Must have
• My Name: Malcolm Ferris, CPA
• Position: Owner
• Phone: (240) 555-0148
• Email: Mferris@rkledgerwise.example
• Website: www.Rkledgerwise.example
• Address: 4736 Ferncliff Ave #2093
• Dunmore Falls, MD 21990
Nice to have
• Same design & color scheme as TM Bookkeepnig Business card sample attached

```html
<!DOCTYPE html>
<html lang="en">
<head>
<meta charset="utf-8">
<title>RK Ledgerwise &amp; Filing Partners – Business Card</title>
<link rel="stylesheet" href="https://fonts.googleapis.com/css2?family=Cinzel:wght@500;600&family=Open+Sans:wght@400&display=swap">
<style>
  :root {
    --brand-blue: #0c5ba6;
    --brand-grey: #5c5c5c;
    --brand-dark: #333333;
    --card-white: #f4f4f4;
    --pure-white: #ffffff;
    --ink: #1e1e1e;
    --page-bg: #c8c8ca;
  }
  * { margin: 0; padding: 0; box-sizing: border-box; }
  html, body { width: 1200px; height: 1200px; overflow: hidden; }
  body { background: var(--page-bg); position: relative; font-family: "Open Sans", Arial, sans-serif; }

  .card { position: absolute; overflow: hidden; }

  /* Front */
  .card-front { left: 208px; top: 94px; width: 780px; height: 447px; background: var(--card-white); }
  .front-wordmark {
    position: absolute; left: 48px; top: 150px;
    font-family: "Cinzel", "Times New Roman", serif; font-weight: 500;
    font-size: 25px; line-height: 38px; letter-spacing: 1px;
    color: var(--brand-blue); white-space: nowrap;
  }
  .front-divider { position: absolute; left: 432px; top: 72px; width: 1px; height: 260px; background: #8a8a8a; }
  .holder { position: absolute; left: 466px; top: 96px; }
  .holder-name {
    font-family: "Cinzel", "Times New Roman", serif; font-weight: 600;
    font-size: 22px; line-height: 28px; color: var(--brand-blue); letter-spacing: .3px;
  }
  .holder-role { font-size: 18px; line-height: 22px; color: var(--ink); }
  .contact-list { position: absolute; left: 464px; top: 180px; list-style: none; }
  .contact-item { display: flex; align-items: flex-start; font-size: 17.5px; line-height: 21px; color: var(--ink); margin-bottom: 8px; }
  .contact-icon { width: 17px; height: 17px; margin-right: 9px; margin-top: 3px; flex: none; }
  .band-blue { position: absolute; left: 0; top: 395px; width: 441px; height: 52px; background: var(--brand-blue); }
  .band-grey { position: absolute; left: 441px; top: 421px; width: 339px; height: 26px; background: var(--brand-grey); }
  .band-fold { position: absolute; left: 441px; top: 395px; width: 25px; height: 26px; }

  /* Back */
  .card-back { left: 213px; top: 632px; width: 771px; height: 444px; background: var(--card-white); }
  .back-field { position: absolute; left: 21px; top: 22px; width: 728px; height: 396px; background: var(--brand-blue);
    display: flex; align-items: center; justify-content: center; }
  .back-wordmark {
    font-family: "Cinzel", "Times New Roman", serif; font-weight: 500;
    font-size: 38px; line-height: 50px; letter-spacing: 2px; color: var(--pure-white); white-space: nowrap;
  }
</style>
</head>
<body>

<section class="card card-front">
  <div class="front-wordmark">RK Ledgerwise<br>&amp; Filing Partners</div>
  <div class="front-divider"></div>

  <div class="holder">
    <div class="holder-name">Malcolm Ferris, CPA</div>
    <div class="holder-role">Owner</div>
  </div>

  <ul class="contact-list">
    <li class="contact-item">
      <svg class="contact-icon" viewBox="0 0 17 17"><rect width="17" height="17" fill="#0c5ba6"/><path d="M6 4 L8 7 L7 8 Q8 10 10 11 L11 10 L13 12 L11.5 13.5 Q6 12 4.5 6 Z" fill="#fff"/></svg>
      <span>(240) 555-0148</span>
    </li>
    <li class="contact-item">
      <svg class="contact-icon" viewBox="0 0 17 17"><rect width="17" height="17" fill="#0c5ba6"/><rect x="3.5" y="5" width="10" height="7.5" fill="none" stroke="#fff" stroke-width="1.2"/><path d="M3.5 5 L8.5 9 L13.5 5" fill="none" stroke="#fff" stroke-width="1.2"/></svg>
      <span>Mferris@rkledgerwise.example</span>
    </li>
    <li class="contact-item">
      <svg class="contact-icon" viewBox="0 0 17 17"><rect width="17" height="17" fill="#0c5ba6"/><circle cx="8.5" cy="8.5" r="5" fill="none" stroke="#fff" stroke-width="1.2"/><path d="M3.5 8.5 H13.5 M8.5 3.5 Q5.5 8.5 8.5 13.5 M8.5 3.5 Q11.5 8.5 8.5 13.5" fill="none" stroke="#fff" stroke-width="1"/></svg>
      <span>www.Rkledgerwise.example</span>
    </li>
    <li class="contact-item">
      <svg class="contact-icon" viewBox="0 0 17 17"><rect width="17" height="17" fill="#0c5ba6"/><path d="M8.5 14 Q4.5 9 4.5 7 A4 4 0 0 1 12.5 7 Q12.5 9 8.5 14 Z" fill="#fff"/><circle cx="8.5" cy="7" r="1.6" fill="#0c5ba6"/></svg>
      <span>4736 Ferncliff Ave #2093<br>Dunmore Falls, MD 21990</span>
    </li>
  </ul>

  <div class="band-blue"></div>
  <svg class="band-fold" viewBox="0 0 25 26"><polygon points="0,0 25,26 0,26" fill="#333333"/></svg>
  <div class="band-grey"></div>
</section>

<section class="card card-back">
  <div class="back-field">
    <div class="back-wordmark">RK Ledgerwise<br>&amp; Filing Partners</div>
  </div>
</section>

</body>
</html>
```